web site to find a reliable, local tradesman, handyman or builder for any job

Design a web site as marketplace for handyman and client.
Handyman can
* set their profile (name, address, contacts)
* search / view / apply for job offers (by setting a new offer)
Client can
* search / view job offers
* generate new job offers (title, description, max price, date, duration, location).
* select and rate a job
Main functions would be SEARCH / VIEW to see in one glance WHAT needs to be done WHERE. The contractors then exchange contacts.
Handyman

```html
<!DOCTYPE html>
<html lang="en">
<head>
<meta charset="utf-8">
<title>Handora – Find a Local Handyman</title>
<link href="https://fonts.googleapis.com/css2?family=Montserrat:wght@600;700&family=Ubuntu:wght@400;500;700&family=Ubuntu+Condensed&family=Open+Sans:wght@400;600;700&display=swap" rel="stylesheet">
<style>
:root{
  --sky:#d9eefb;
  --sky-light:#eef7fd;
  --navy:#27478e;
  --nav-top:#4a6db8;
  --nav-bottom:#2d4f9a;
  --blue-btn:#1e8fe0;
  --orange:#f7921e;
  --orange-dark:#ec7a0a;
  --orange-light:#ffb347;
  --text:#333;
  --muted:#666;
  --line:#d6d6d6;
  --panel:#e7f0fc;
  --link:#1d4f9c;
}
*{box-sizing:border-box;margin:0;padding:0}
html,body{width:1200px;height:1003px;overflow:hidden}
body{position:relative;font-family:"Ubuntu",sans-serif;color:var(--text);
  background:linear-gradient(#dff0fb 0,#f4faff 250px,#fff 500px,#fff 510px,#e3ebfa 520px,#f5f8fe 700px,#fff 880px)}
.abs{position:absolute}
a{color:inherit;text-decoration:none}

/* top bar */
.topbar{left:0;top:0;width:1200px;height:26px;background:#fff;border-bottom:1px solid #e3eef7}
.toplinks{right:186px;top:6px;display:flex;font:11px "Open Sans",sans-serif;color:#777}
.toplinks a{padding:0 19px;border-left:1px solid #ccc;line-height:11px}
.toplinks a:first-child{border:none}
.toplinks .active{color:var(--navy);font-weight:600}
.toplinks .login{color:var(--link)}

/* header */
.brand{left:174px;top:56px;display:flex;align-items:center;gap:8px;font:700 32px "Ubuntu",sans-serif;color:var(--navy)}
.brand-dot{width:18px;height:18px;border-radius:50%;background:var(--navy)}
.btn{display:flex;align-items:center;justify-content:center;border-radius:3px;font:700 16px "Montserrat",sans-serif;color:#fff;letter-spacing:.3px;white-space:nowrap}
.btn-hire{left:568px;top:56px;width:225px;height:35px;background:linear-gradient(#3fa9f0,#1c7fd6);border:1px solid #176cc0;justify-content:flex-start;padding-left:26px;font-size:14px;letter-spacing:0}
.btn-post{left:800px;top:56px;width:225px;height:35px;background:linear-gradient(#ffb238,#f57c00);border:1px solid #e07000;font-size:15px}
.hire-art{left:746px;top:43px;width:44px;height:54px;border-radius:22px 22px 4px 4px;background:linear-gradient(#f2d2b0,#3c6cc0)}

/* nav */
.mainnav{left:174px;top:121px;width:851px;height:41px;border-radius:3px;background:linear-gradient(var(--nav-top),var(--nav-bottom));display:flex;align-items:center}
.mainnav a{color:#fff;font:400 17px "Ubuntu",sans-serif;padding:0 26px;line-height:41px;border-right:1px solid #25448a;box-shadow:1px 0 0 #5b7dc4}
.mainnav a:first-child{padding-left:25px}
.create{left:893px;top:128px;width:124px;height:27px;border:1px solid #7d9bd8;border-radius:3px;background:linear-gradient(#4d70bb,#2f519c);color:#fff;font:16px "Ubuntu",sans-serif;display:flex;align-items:center;justify-content:center}

/* search panel */
.search-panel{left:174px;top:195px;width:225px;height:278px;border:2px solid var(--orange);border-radius:5px;background:#fff}
.search-head{left:0;top:0;width:221px;height:40px;background:linear-gradient(var(--orange-light),var(--orange-dark));color:#fff;font:700 14px "Open Sans",sans-serif;padding:12px 10px;border-radius:3px 3px 0 0}
.search-art{left:158px;top:-20px;width:56px;height:58px;border-radius:28px;background:linear-gradient(#cfe0f2,#f5f9fd);border:1px solid #e6eef6}
.field-label{left:8px;font:13.5px "Ubuntu",sans-serif;color:#333}
.field{left:8px;width:206px;height:28px;border:1px solid #ccc;border-radius:2px;background:linear-gradient(#f6f6f6,#e9e9e9);font:12px "Open Sans",sans-serif;color:#999;padding:6px 10px}
.field.plain{background:#fff}
.field .caret{position:absolute;right:0;top:0;width:28px;height:26px;border-left:1px solid #ccc;background:#fbfbfb}
.field .caret::after{content:"";position:absolute;left:10px;top:11px;border:4px solid transparent;border-top:5px solid #444}
.btn-search{left:8px;top:234px;width:207px;height:33px;background:linear-gradient(#ffab2e,#f57a00);border:1px solid #e07000;border-radius:3px;font-size:15px;gap:6px}

/* hero */
.hero-title{left:418px;top:191px;width:610px;text-align:center;font:700 32px "Montserrat",sans-serif;color:#1f4a9c;letter-spacing:2px}
.hero-rule{top:209px;height:1px;background:#c8dff0}
.hero-sub{left:418px;top:230px;width:610px;text-align:center;font:27px "Ubuntu Condensed",sans-serif;color:#f08a16}
.hero-sub b{font-weight:700;font-size:29px}
.step{top:276px;width:195px;height:200px;background:linear-gradient(#e3f0f9,#fff 45%);text-align:center}
.step.featured{background:linear-gradient(#fbc888,#fff 55%)}
.step svg{margin-top:30px}
.step h3{position:absolute;left:0;width:100%;top:128px;font:500 14px "Ubuntu",sans-serif;color:#222}
.step p{position:absolute;left:0;width:100%;top:155px;font:10px/12px "Open Sans",sans-serif;color:#222}

/* job bar */
.band{left:0;top:509px;width:1200px;height:3px;background:#4e77cd}
.jobbar{left:175px;top:512px;width:850px;height:38px;background:linear-gradient(#4f71ba,#2f509b);border-radius:0 0 3px 3px}
.jobbar-title{left:55px;top:7px;color:#fff;font:700 19px "Open Sans",sans-serif}
.job-select{left:243px;top:3px;width:465px;height:27px;background:#fff;border:1px solid #bfcbe2;border-radius:2px;font:16px "Open Sans",sans-serif;color:#999;padding:2px 8px}
.adv{position:absolute;right:42px;top:4px;padding:1px 8px;background:#eef0f3;border:1px solid #ddd;font:600 10px "Open Sans",sans-serif;color:#1d4f9c}
.job-select .caret{position:absolute;right:0;top:0;width:32px;height:25px;border-left:1px solid #ccc}
.job-select .caret::after{content:"";position:absolute;left:11px;top:10px;border:4px solid transparent;border-top:5px solid #444}
.btn-go{left:716px;top:3px;width:130px;height:28px;background:linear-gradient(#3d63b8,#223f86);border:1px solid #6f8fd0;font-size:15px}

/* map */
.map-frame{left:174px;top:581px;width:225px;height:219px;background:#fff;border:1px solid #e4e8ee;border-radius:5px;padding:5px}
.map{width:213px;height:207px;background:linear-gradient(135deg,#e2e2dc,#ecebe2 50%,#dcdbd2)}
.map-label{left:76px;top:78px;background:#fff;border:1px solid #ccc;padding:4px 8px;font:13px "Open Sans",sans-serif;color:#333}

/* categories */
.tab{top:583px;height:35px;font:15px "Ubuntu",sans-serif;padding:9px 12px;white-space:nowrap}
.tab-active{left:422px;width:155px;background:linear-gradient(#4f71ba,#2f509b);color:#fff;border-radius:4px 0 0 0;clip-path:polygon(0 0,88% 0,100% 100%,0 100%)}
.tab-idle{left:570px;width:176px;background:#eceef2;color:#222;padding-left:26px;clip-path:polygon(0 0,88% 0,100% 100%,12% 100%)}
.cat-panel{left:417px;top:617px;width:609px;height:180px;background:linear-gradient(#e3edfc,#f7f9fe)}
.cat-list{top:630px;width:129px;list-style:none}
.cat-list li{height:30px;line-height:30px;border-bottom:1px dashed #d7dde6;font:10px "Open Sans",sans-serif;color:#333;padding-left:10px;position:relative;white-space:nowrap}
.cat-list li::before{content:"›";position:absolute;left:0;top:0;font-size:11px}
.cat-list li.hover{background:#d5e1f4;color:var(--link)}
.cat-sep{top:650px;width:1px;height:185px;border-left:1px dashed #e0e5ec}

/* footer */
.footer{left:0;top:882px;width:1200px;height:62px;background:linear-gradient(#f6f8fb,#edf0f4);border-top:1px solid #e2e6ec;border-bottom:1px solid #dde2e8}
.footnav{left:0;top:908px;width:1200px;display:flex;justify-content:center;font:10px "Open Sans",sans-serif;color:#555}
.footnav a{padding:0 25px;border-left:1px solid #777;line-height:11px}
.footnav a:first-child{border:none}
.footnav .u{text-decoration:underline}
.legal{left:0;top:959px;width:1200px;text-align:center;font:9.5px "Open Sans",sans-serif;color:#555}
.legal span{text-decoration:underline}
</style>
</head>
<body>

<div class="abs topbar"></div>
<nav class="abs toplinks">
  <a class="active" href="#">Home</a><a href="#">About us</a><a href="#">Privacy Policy</a><a class="login" href="#">Login</a><a href="#">Contact us</a>
</nav>

<div class="abs brand"><span class="brand-dot"></span>Handora</div>
<a class="abs btn btn-hire" href="#">HIRE A HANDYMAN</a>
<div class="abs hire-art" role="img" aria-label="Illustrated handyman mascot in cap and overalls"></div>
<a class="abs btn btn-post" href="#">POST YOUR JOB</a>

<nav class="abs mainnav">
  <a href="#">Find Handyman</a><a href="#">Find Work</a><a href="#">How its Work?</a>
</nav>
<a class="abs create" href="#">Create account</a>

<section class="abs search-panel">
  <div class="abs search-head">Search Handyman</div>
  <div class="abs search-art" role="img" aria-label="Illustrated handyman holding a wrench"></div>
  <div class="abs field-label" style="top:56px">Select Supplier</div>
  <div class="abs field" style="top:76px">All<span class="caret"></span></div>
  <div class="abs field-label" style="top:115px">Select Location</div>
  <div class="abs field" style="top:135px">London<span class="caret"></span></div>
  <div class="abs field-label" style="top:174px">Enter Post Code</div>
  <div class="abs field plain" style="top:194px">00000</div>
  <a class="abs btn btn-search" href="#">
    <svg width="13" height="13" viewBox="0 0 13 13"><circle cx="5.5" cy="5.5" r="4" fill="none" stroke="#fff" stroke-width="2"/><path d="M8.5 8.5l3.5 3.5" stroke="#fff" stroke-width="2"/></svg>SEARCH</a>
</section>

<div class="abs hero-rule" style="left:416px;width:80px"></div>
<div class="abs hero-rule" style="left:948px;width:80px"></div>
<h1 class="abs hero-title">GET YOUR WORK DONE</h1>
<p class="abs hero-sub">in just <b>3</b> simple steps</p>

<div class="abs step" style="left:419px">
  <svg width="40" height="56" viewBox="0 0 40 56"><circle cx="20" cy="18" r="14" fill="none" stroke="#2566c8" stroke-width="5"/><path d="M20 32v22M10 44h20" stroke="#2566c8" stroke-width="5"/></svg>
  <h3>1.Lorem Ipsum Dolor</h3>
  <p>Ut wisi enim ad minim veniam,<br>quis nostrud exerci</p>
</div>
<div class="abs step featured" style="left:623px">
  <svg width="44" height="72" viewBox="0 0 44 72"><path d="M22 3a18 18 0 0 0-11 32c3 3 4 7 4 12h14c0-5 1-9 4-12A18 18 0 0 0 22 3z" fill="none" stroke="#e57b0c" stroke-width="2.5"/><path d="M17 46V30l5 5 5-5v16" fill="none" stroke="#e57b0c" stroke-width="2"/><path d="M15 51h14M15 56h14M18 61h8" stroke="#e57b0c" stroke-width="3"/></svg>
  <h3>2.Lorem Ipsum Dolor</h3>
  <p>Ut wisi enim ad minim veniam,<br>quis nostrud exerci</p>
</div>
<div class="abs step" style="left:827px">
  <svg width="56" height="56" viewBox="0 0 56 56"><path d="M2 30l8-6 10 10L50 4l4 4-33 44z" fill="#2566c8"/></svg>
  <h3>3.Lorem Ipsum Dolor</h3>
  <p>Ut wisi enim ad minim veniam,<br>quis nostrud exerci</p>
</div>

<div class="abs band"></div>
<section class="abs jobbar">
  <svg class="abs" style="left:15px;top:3px" width="28" height="30" viewBox="0 0 28 30"><circle cx="12" cy="12" r="9" fill="none" stroke="#8fb3ee" stroke-width="3.5"/><path d="M18 19l7 8" stroke="#8fb3ee" stroke-width="4" stroke-linecap="round"/></svg>
  <div class="abs jobbar-title">Looking For Job?</div>
  <div class="abs job-select">Select your job type<span class="adv">Advanced Search</span><span class="caret"></span></div>
  <a class="abs btn btn-go" href="#">GO &amp; FIND</a>
</section>

<div class="abs map-frame">
  <div class="map" role="img" aria-label="Street map of the city centre showing nearby handyman locations"></div>
  <div class="abs map-label">UNITED STATE</div>
</div>

<div class="abs cat-panel"></div>
<div class="abs tab tab-active">Popular Categories</div>
<div class="abs tab tab-idle">Top 10 Handyman</div>
<div class="abs cat-sep" style="left:592px"></div>
<div class="abs cat-sep" style="left:772px"></div>
<ul class="abs cat-list" style="left:437px">
  <li>Lorem ipsum</li><li>dolor sit amet</li><li>consectetuer adipiscing</li><li>sed diam nonummy</li><li>nibh euismod</li><li>tincidunt ut laoreet</li><li>dolore magna</li>
</ul>
<ul class="abs cat-list" style="left:617px">
  <li>Lorem ipsum</li><li>dolor sit amet</li><li class="hover">consectetuer adipiscing</li><li>sed diam nonummy</li><li>nibh euismod</li><li>tincidunt ut laoreet</li><li>dolore magna</li>
</ul>
<ul class="abs cat-list" style="left:797px">
  <li>Lorem ipsum</li><li>dolor sit amet</li><li>consectetuer adipiscing</li><li>sed diam nonummy</li>
</ul>

<footer>
  <div class="abs footer"></div>
  <nav class="abs footnav">
    <a href="#">Home</a><a class="u" href="#">Get Quotes</a><a href="#">Become a Supplier</a><a href="#">FAQ's</a><a href="#">Testimonials</a><a href="#">About Us</a><a href="#">Site map</a><a href="#">Contact Us</a>
  </nav>
  <p class="abs legal">© 2011 Company Name . Use of this Web site constitutes acceptance of the Company name <span>User Agreement and incorporated Policies.</span></p>
</footer>

</body>
</html>
```